Marketing Flyer for General Contractor

1. General Layout: 8.5" x 11
Front Page: Introduce our services with a strong, attention-grabbing header. Use icons or special bullet points to list the services, making them stand out. (See PDf for content)
Back Page: Provide detailed descriptions and benefits, organized in a clean and structured manner. Include testimonials or client success stories if available. (See PDF for Content)
2. Design Elements:
Color Scheme: Incorporate blue, black, white, red, yellow, and turquoise. Additional colors can be used if they enhance the design.
Icons/Bullet Points: Use creative and visually appealing icons or bullet points for the services list on the front page.
Images: Use the uploaded images and incorporate high-quality stock images where necessary. I am willing to purchase stock images if they enhance the layout.
QR Code: Include a QR code with the phone number and website in the footer on both pages.
Contact Info: Ensure the contact information stands out and is easy to find and read.
3. Specific Instructions for Content:
Front Page:
Header: Create a bold and eye-catching title that communicates our expertise in helping realtors enhance listings.
Services List: Use icons or special bullet points to make each service stand out. Ensure the text is clear and easy to read.
Contact Info: Prominently display the phone number and website, with a QR code at the bottom.
Back Page:
Detailed Descriptions: Organize the content logically, using headings and subheadings to break up the text. Make it easy to scan and read.
Benefits and Value Statements: Highlight the key benefits and value propositions in bold or larger font to draw attention.
Testimonials/Success Stories: If space allows, include one or two testimonials or success stories.
Contact Info: Again, prominently display the phone number and website, with a QR code at the bottom.
4. Typography:
Use clear, readable fonts. Mix bold and regular fonts to emphasize key points and maintain a professional look.
5. Additional Notes:
Ensure the overall design is balanced and not too cluttered.
Maintain a professional yet inviting aesthetic that appeals to realtors.
The flyer should convey confidence and expertise, encouraging realtors to choose our services.
Low design quality
Real estate agents
Construction General Contractor

```html
<!DOCTYPE html>
<html lang="en">
<head>
<meta charset="utf-8">
<title>Harbor Crest Remodel – Realtor Flyer</title>
<link rel="stylesheet" href="https://fonts.googleapis.com/css2?family=Poppins:ital,wght@0,400;0,500;0,600;0,700;0,800;1,600;1,700&display=swap">
<style>
  :root{
    --backdrop:#a9abad;
    --paper:#ffffff;
    --blue:#1f4fa3;
    --blue-dark:#163a7a;
    --red:#ea4a4a;
    --red-dark:#d63a3a;
    --yellow:#ffd23a;
    --ink:#1d1d1f;
    --muted:#5b5f66;
    --band:#e9ebee;
  }
  *{box-sizing:border-box;margin:0;padding:0}
  html,body{width:1200px;height:2316px;overflow:hidden}
  body{background:var(--backdrop);font-family:'Poppins',sans-serif;color:var(--ink);position:relative}
  .page{position:absolute;left:220px;width:760px;height:984px;background:var(--paper);box-shadow:0 6px 18px rgba(0,0,0,.25);overflow:hidden}
  .page--front{top:150px}
  .page--back{top:1190px}

  /* front */
  .hero-photo{position:absolute;left:0;top:0;width:760px;height:350px;background:linear-gradient(100deg,#ffffff 0%,#f1f3f5 30%,#dfe4ea 60%,#c9d2dc 100%)}
  .brand{position:absolute;left:38px;top:34px;display:flex;align-items:center;gap:10px;font-weight:700;font-size:17px;color:var(--blue-dark);letter-spacing:.5px}
  .brand__mark{width:22px;height:22px;background:var(--blue-dark);border-radius:50%}
  .hero-band{position:absolute;left:0;top:350px;width:760px;height:96px;background:var(--paper)}
  .hero-band__left{position:absolute;left:0;top:0;width:420px;height:96px;background:var(--blue);clip-path:polygon(0 0,100% 0,88% 100%,0 100%);padding:14px 0 0 42px;color:#fff}
  .hero-band__title{font-style:italic;font-weight:700;font-size:30px;line-height:1.15}
  .hero-band__sub{font-size:14px;font-weight:500;opacity:.9}
  .hero-band__offer{position:absolute;right:40px;top:16px;text-align:right;color:var(--blue-dark);font-weight:800;font-size:30px;line-height:1.05;text-transform:uppercase}
  .services{position:absolute;left:0;top:446px;width:760px;height:420px;background:var(--red);padding:22px 46px}
  .tag{display:block;width:max-content;margin:0 auto;background:var(--yellow);color:var(--ink);font-weight:800;font-size:16px;padding:5px 22px;text-transform:uppercase;letter-spacing:.5px}
  .services__grid{display:grid;grid-template-columns:repeat(3,1fr);row-gap:34px;column-gap:18px;margin-top:30px}
  .service{display:flex;align-items:center;gap:12px;color:#fff;font-weight:600;font-size:15px;line-height:1.25}
  .service svg{flex:none;width:46px;height:46px}
  .footer{position:absolute;left:0;bottom:0;width:760px;height:118px;background:var(--paper);padding:22px 40px;display:flex;align-items:center;justify-content:space-between}
  .footer__cta{font-size:12px;font-weight:600;color:var(--muted);letter-spacing:1px;margin-left:58px}
  .footer__phone{display:flex;align-items:center;gap:12px;font-weight:800;font-size:40px;color:var(--blue-dark);line-height:1}
  .footer__phone svg{width:46px;height:46px}
  .footer__links{font-size:13px;font-weight:600;color:var(--ink);line-height:1.7;text-align:left}

  /* back */
  .accent-arc{position:absolute;left:-60px;top:40px;width:180px;height:180px;border-radius:50%;background:var(--red)}
  .intro-photo{position:absolute;left:40px;top:70px;width:320px;height:320px;border-radius:50%;background:radial-gradient(circle at 40% 40%,#f5efe6,#d9c7ae 60%,#b89b78);border:8px solid #fff}
  .intro{position:absolute;left:390px;top:70px;width:340px}
  .intro h3{color:var(--red);font-size:14px;font-weight:700;text-transform:uppercase;margin-bottom:4px}
  .intro p{font-size:11.5px;color:var(--muted);line-height:1.5;margin-bottom:14px}
  .solution{position:absolute;left:0;top:450px;width:760px;height:190px;background:var(--band);text-align:center;padding:26px 70px 0}
  .solution h2{color:var(--blue-dark);font-size:24px;font-weight:800;text-transform:uppercase}
  .solution p{font-size:12px;color:var(--muted);line-height:1.5;margin:8px 0 16px}
  .steps{position:absolute;left:0;top:640px;width:760px;height:226px;background:var(--red);padding:46px 40px 0;display:grid;grid-template-columns:repeat(3,1fr);gap:22px}
  .step{position:relative;background:#fff;padding:36px 16px 14px;text-align:center;height:160px}
  .step__num{position:absolute;left:50%;top:-26px;transform:translateX(-50%);width:52px;height:52px;border-radius:50%;background:var(--blue-dark);color:#fff;font-weight:800;font-size:18px;display:flex;align-items:center;justify-content:center;border:4px solid #fff}
  .step h4{font-size:14px;font-weight:700;color:var(--ink);margin-bottom:6px}
  .step p{font-size:10.5px;color:var(--muted);line-height:1.45}
  .solution .tag{margin-top:0}
</style>
</head>
<body>

<section class="page page--front">
  <div class="hero-photo" role="img" aria-label="Bright modern living room with white sofa and large windows"></div>
  <div class="brand"><span class="brand__mark"></span>HARBOR CREST REMODEL</div>

  <div class="hero-band">
    <div class="hero-band__left">
      <div class="hero-band__title">Remodeling Experts</div>
      <div class="hero-band__sub">Boston's #1 General Contractor</div>
    </div>
    <div class="hero-band__offer">Remodel Now<br>Pay at Closing</div>
  </div>

  <div class="services">
    <span class="tag">Specializing In</span>
    <div class="services__grid">
      <div class="service"><svg viewBox="0 0 46 46" fill="none" stroke="#fff" stroke-width="2.5"><rect x="8" y="14" width="30" height="24"/><path d="M8 22h30M16 8v6M30 8v6"/></svg>Kitchen<br>Remodel</div>
      <div class="service"><svg viewBox="0 0 46 46" fill="none" stroke="#fff" stroke-width="2.5"><path d="M6 24h34v6a8 8 0 0 1-8 8H14a8 8 0 0 1-8-8z"/><path d="M12 24V10a4 4 0 0 1 8 0"/></svg>Bathroom<br>Remodel</div>
      <div class="service"><svg viewBox="0 0 46 46" fill="none" stroke="#fff" stroke-width="2.5"><rect x="8" y="8" width="26" height="10" rx="2"/><path d="M34 13h4v10H22v6M22 29v10"/></svg>Painting:<br>Interior/Exterior</div>
      <div class="service"><svg viewBox="0 0 46 46" fill="none" stroke="#fff" stroke-width="2.5"><rect x="6" y="6" width="34" height="34"/><path d="M6 17h34M6 28h34M20 6v11M28 17v11M16 28v12"/></svg>Flooring:<br>Carpet, Vinyl, Wood</div>
      <div class="service"><svg viewBox="0 0 46 46" fill="none" stroke="#fff" stroke-width="2.5"><rect x="8" y="6" width="30" height="34"/><path d="M23 6v34M8 23h30"/></svg>Window and door<br>Replacement</div>
      <div class="service"><svg viewBox="0 0 46 46" fill="none" stroke="#fff" stroke-width="2.5"><path d="M26 4 12 26h10l-2 16 14-22H24z"/></svg>Energy-Efficient<br>Upgrades</div>
      <div class="service"><svg viewBox="0 0 46 46" fill="none" stroke="#fff" stroke-width="2.5"><path d="M4 22h38M8 22v18M38 22v18M8 30h30M14 22V10h18v12"/></svg>Deck &amp; Patio<br>Construction</div>
      <div class="service"><svg viewBox="0 0 46 46" fill="none" stroke="#fff" stroke-width="2.5"><path d="M4 20 23 6l19 14v20H4z"/><path d="M12 40V24h22v16M12 30h22"/></svg>Garage<br>Renovation</div>
      <div class="service"><svg viewBox="0 0 46 46" fill="none" stroke="#fff" stroke-width="2.5"><path d="M23 42V20M23 6c8 4 10 14 0 18-10-4-8-14 0-18zM8 42h30"/></svg>Landscaping</div>
    </div>
  </div>

  <footer class="footer">
    <div>
      <div class="footer__cta">CALL • TEXT • BOOK ONLINE</div>
      <div class="footer__phone"><svg viewBox="0 0 46 46"><circle cx="23" cy="23" r="22" fill="#163a7a"/><path d="M16 12l5 5-3 4a16 16 0 0 0 7 7l4-3 5 5-3 4c-10 0-19-9-19-19z" fill="#fff"/></svg>555-014-2290</div>
    </div>
    <div class="footer__links">www.harborcrestremodel.com<br>info@harborcrestremodel.com</div>
  </footer>
</section>

<section class="page page--back">
  <div class="accent-arc"></div>
  <div class="intro-photo" role="img" aria-label="Renovated white kitchen with island and pendant lights"></div>
  <div class="intro">
    <h3>The Agent's Trusted and Reliable Partner</h3>
    <p>Elevate your reputation with a partner that is dedicated to your success. Our team brings fast, quality work and transparent pricing to every project.</p>
    <h3>A Turnkey Solution for Every Listing</h3>
    <p>We handle the whole job for you, from design and permits to materials, labor and project management, delivering listings that sell faster.</p>
    <h3>Fix Now, Sellers Pay at Closing</h3>
    <p>Keep listings moving with no upfront cost. Sellers pay for approved work out of the proceeds at closing, so every deal stays on track.</p>
  </div>

  <div class="solution">
    <h2>You Go-To Solution for Every Listing</h2>
    <p>Harbor Crest Remodel is ready to start work on your listings immediately, whether big or small. Our team of skilled professionals handles every detail to maximize value.</p>
    <span class="tag">Get Started in 3 Simple Steps</span>
  </div>

  <div class="steps">
    <div class="step"><div class="step__num">01</div><h4>Request Free Estimate</h4><p>Schedule a quick walkthrough and receive a clear, itemized quote within two days.</p></div>
    <div class="step"><div class="step__num">02</div><h4>Harbor Crest Gets to Work</h4><p>Our crew completes the approved work on schedule while you keep marketing the home.</p></div>
    <div class="step"><div class="step__num">03</div><h4>Relist and Close</h4><p>The home sells for more and the remodel cost is paid from proceeds at closing.</p></div>
  </div>

  <footer class="footer">
    <div>
      <div class="footer__cta">CALL • TEXT • BOOK ONLINE</div>
      <div class="footer__phone"><svg viewBox="0 0 46 46"><circle cx="23" cy="23" r="22" fill="#163a7a"/><path d="M16 12l5 5-3 4a16 16 0 0 0 7 7l4-3 5 5-3 4c-10 0-19-9-19-19z" fill="#fff"/></svg>555-014-2290</div>
    </div>
    <div class="footer__links">www.harborcrestremodel.com<br>info@harborcrestremodel.com</div>
  </footer>
</section>

</body>
</html>
```